Bramblecrest Apparel and Nutrition is looking for a Clothing/Supplement Online Store Website!

Must be convenient, and user friendly, with vibrant colors that catch the eye!

Target Market(s)

Athletes, and Fashion Customers

Industry/Entity Type

Fitness

Coding

Coded - Design and coding required

Number of Pages Required

3 page

Font styles to use
Decorative

Colors

Designer to choose colors to be used in the design.

Requirements
Must have
• Somewhere to feature products, features to promote discounts and make announcements.
Nice to have
• My logos on each page

```html
<!DOCTYPE html>
<html lang="en">
<head>
<meta charset="utf-8">
<title>Bramblecrest Apparel and Nutrition</title>
<link href="https://fonts.googleapis.com/css2?family=BenchNine:wght@300;400&family=Bebas+Neue&family=Lato:wght@400;700&display=swap" rel="stylesheet">
<style>
:root{
  --ink:#1d1d1d;
  --text:#333;
  --muted:#777;
  --topbar:#4b4b4b;
  --panel:#f2f2f2;
  --footer:#f5f5f5;
  --bottom:#e8e8e8;
  --line:#e2e2e2;
  --white:#fff;
}
*{margin:0;padding:0;box-sizing:border-box}
html,body{width:1200px;height:3606px;overflow:hidden;background:var(--white)}
body{position:relative;font-family:'Lato',sans-serif;color:var(--text)}
.abs{position:absolute}
.thin{font-family:'BenchNine',sans-serif;font-weight:300;color:var(--ink);text-transform:uppercase;line-height:1}
.btn-dark{position:absolute;background:var(--ink);color:var(--white);font-family:'BenchNine',sans-serif;font-weight:300;display:flex;align-items:center;justify-content:center;text-transform:uppercase}

.topbar{left:0;top:0;width:1200px;height:30px;background:var(--topbar);color:var(--white);font-size:11px;font-weight:700}
.topbar .note{position:absolute;left:0;width:1200px;top:9px;text-align:center}
.topbar .phone{position:absolute;left:938px;top:8px;display:flex;align-items:center;gap:6px;font-size:12px}

.nav{left:0;top:30px;width:1200px;height:75px;border-bottom:1px solid var(--line)}
.logo{position:absolute;left:162px;top:24px;display:flex;align-items:center;gap:8px;font-family:'Lato',sans-serif;font-weight:700;font-size:24px;color:var(--ink);letter-spacing:1px}
.logo .mark{width:14px;height:14px;background:var(--ink)}
.menu{position:absolute;top:30px;font-size:11px;color:#555;text-transform:uppercase}
.menu.active{color:var(--ink);font-weight:700}
.navicons{position:absolute;left:955px;top:28px;display:flex;gap:16px}

.hero{left:0;top:105px;width:1200px;height:637px;background:linear-gradient(100deg,#9a7a6c 0%,#b49486 35%,#8c6f64 55%,#6e5a55 100%)}
.hero-card{left:161px;top:217px;width:353px;height:403px;background:#1e1e1e;border:2px solid #1e1e1e}
.hero-card .inner{position:absolute;inset:7px;border:1px solid #cfcfcf}
.hero-card .t1{position:absolute;width:100%;top:50px;text-align:center;font-size:56px;color:var(--white)}
.hero-card .t2{position:absolute;width:100%;top:100px;text-align:center;font-family:'Bebas Neue',sans-serif;font-size:94px;color:var(--white);line-height:1}
.hero-card .t3{position:absolute;width:100%;top:206px;text-align:center;font-family:'Bebas Neue',sans-serif;font-size:38px;color:var(--white);line-height:1}
.hero-card .t4{position:absolute;width:100%;top:255px;text-align:center;font-size:12px;color:var(--white)}
.hero-card .shop{position:absolute;left:107px;top:293px;width:150px;height:51px;background:var(--white);color:var(--ink);font-family:'BenchNine',sans-serif;font-weight:300;font-size:30px;display:flex;align-items:center;justify-content:center}

.feature{position:absolute;top:770px;width:210px;text-align:center}
.feature svg{display:block;margin:0 auto;height:52px}
.feature h3{font-size:13px;font-weight:700;color:var(--ink);margin-top:15px;text-transform:uppercase}
.feature p{font-size:11px;color:var(--muted);line-height:19px;margin-top:12px}

.promo{position:absolute;left:161px;width:878px;height:438px;background:var(--panel)}
.promo .photo{position:absolute;top:0;width:439px;height:438px}
.promo h2{position:absolute;font-size:56px}
.promo h3{position:absolute;font-size:32px;font-weight:700;color:var(--ink)}
.promo p{position:absolute;width:320px;font-size:10px;line-height:19.5px;color:var(--muted)}
.promo .btn-dark{width:150px;height:52px;font-size:30px}

.latest{left:0;width:1200px;top:1981px;text-align:center;font-size:10px;letter-spacing:4px;font-weight:700;color:#555}
.featured-title{left:0;width:1200px;top:2000px;text-align:center;font-size:50px}
.arrow{position:absolute;top:2214px;width:44px;height:44px;border-radius:50%;background:#f0f0f0;display:flex;align-items:center;justify-content:center}
.product{position:absolute;top:2066px;width:200px;text-align:center}
.product .thumb{width:160px;height:175px;margin:0 auto}
.product .name{font-size:13px;line-height:20px;color:var(--text);margin-top:20px;height:42px}
.product .price{font-size:12px;font-weight:700;color:var(--ink);margin-top:4px}
.product .price s{font-weight:400;color:#888;margin-left:12px}
.product .off{font-size:11px;font-weight:700;color:var(--ink);margin-top:6px}
.product .cart{position:relative;margin:12px auto 0;width:122px;height:38px;background:var(--ink);color:var(--white);font-family:'BenchNine',sans-serif;font-weight:300;font-size:24px;display:flex;align-items:center;justify-content:center}

.category{position:absolute;top:2492px;width:270px;text-align:center}
.category .photo{height:238px}
.category .label{font-size:38px;margin-top:14px}

.insta-title{left:0;width:1200px;top:2870px;text-align:center;font-size:50px}
.insta{position:absolute;top:2947px;width:188px;height:186px}

.footer{left:0;top:3147px;width:1200px;height:399px;background:var(--footer)}
.news-title{position:absolute;left:161px;top:40px;font-size:50px}
.news-sub{position:absolute;left:162px;top:102px;width:350px;font-size:13px;font-weight:700;color:var(--ink);line-height:22px}
.news-input{position:absolute;left:521px;top:62px;width:348px;height:41px;background:var(--white);border:1px solid var(--line);font-size:10px;color:#555;padding:14px 10px}
.news-btn{left:883px;top:62px;width:139px;height:41px;font-size:24px}
.footer .rule{position:absolute;left:161px;top:165px;width:878px;height:1px;background:var(--line)}
.fcol{position:absolute;top:207px}
.fcol h4{font-size:13px;font-weight:700;color:var(--ink);text-transform:uppercase}
.fcol a{display:block;font-size:12px;color:#666;text-decoration:none;margin-top:13px}
.fcol h4 + a{margin-top:20px}
.pay{position:absolute;width:36px;height:21px;border-radius:2px}

.bottom{left:0;top:3546px;width:1200px;height:60px;background:var(--bottom)}
.bottom .copy{position:absolute;left:162px;top:23px;font-size:10px;color:#555}
.social{position:absolute;top:12px;width:33px;height:33px;border-radius:50%;background:var(--white)}
.social.first{background:var(--ink)}
</style>
</head>
<body>

<header>
  <div class="abs topbar">
    <div class="note">LOREM IPSUM IS SIMPLY DUMMY TEXT</div>
    <div class="phone">
      <svg width="12" height="12" viewBox="0 0 24 24"><path d="M6.6 10.8a15 15 0 0 0 6.6 6.6l2.2-2.2c.3-.3.7-.4 1-.2 1.1.4 2.3.6 3.6.6.6 0 1 .4 1 1V20c0 .6-.4 1-1 1A17 17 0 0 1 3 4c0-.6.4-1 1-1h3.5c.6 0 1 .4 1 1 0 1.3.2 2.5.6 3.6.1.3 0 .7-.2 1z" fill="#fff"/></svg>
      555 014 7720
    </div>
  </div>
  <nav class="abs nav">
    <div class="logo"><span class="mark"></span>BRAMBLECREST</div>
    <span class="menu active" style="left:418px">Home</span>
    <span class="menu" style="left:494px">Men</span>
    <span class="menu" style="left:559px">Woman</span>
    <span class="menu" style="left:646px">About</span>
    <span class="menu" style="left:726px">Contact</span>
    <div class="navicons">
      <svg width="16" height="16" viewBox="0 0 24 24" fill="none" stroke="#888" stroke-width="1.5"><circle cx="12" cy="8" r="4"/><path d="M4 21c0-4 4-7 8-7s8 3 8 7"/></svg>
      <svg width="17" height="16" viewBox="0 0 24 24" fill="none" stroke="#888" stroke-width="1.5"><path d="M12 20s-8-5-8-11a4.5 4.5 0 0 1 8-2.8A4.5 4.5 0 0 1 20 9c0 6-8 11-8 11z"/></svg>
      <svg width="18" height="16" viewBox="0 0 24 24" fill="none" stroke="#888" stroke-width="1.5"><path d="M2 3h3l3 12h11l2-8H6"/><circle cx="9" cy="19" r="1.5"/><circle cx="18" cy="19" r="1.5"/></svg>
    </div>
  </nav>
</header>

<section class="abs hero" role="img" aria-label="Three smiling women in sports bras leaning against a brick wall">
</section>
<div class="abs hero-card">
  <div class="inner"></div>
  <div class="thin t1">Best</div>
  <div class="t2">SELLER</div>
  <div class="t3">SALE UP TO 50% OFF</div>
  <div class="t4">Offer Valid 5 SEP</div>
  <div class="shop">SHOP NOW</div>
</div>

<section class="features">
  <div class="feature" style="left:151px">
    <svg viewBox="0 0 72 40" width="72" fill="none" stroke="#222" stroke-width="1.6"><rect x="14" y="6" width="32" height="22"/><path d="M46 12h12l8 9v7H46"/><circle cx="24" cy="31" r="4"/><circle cx="56" cy="31" r="4"/><path d="M2 12h9M5 18h7M2 24h9"/></svg>
    <h3>Free Delivery</h3>
    <p>Lorem Ipsum is simply dummy text<br>of the printing and typesetting.</p>
  </div>
  <div class="feature" style="left:378px">
    <svg viewBox="0 0 40 44" width="40" fill="none" stroke="#222" stroke-width="1.6"><path d="M20 2 36 8v12c0 11-7 18-16 22C11 38 4 31 4 20V8z"/><path d="M13 22l5 5 9-10"/></svg>
    <h3>Safe and Secure</h3>
    <p>Lorem Ipsum is simply dummy text<br>of the printing and typesetting.</p>
  </div>
  <div class="feature" style="left:606px">
    <svg viewBox="0 0 48 48" width="48" fill="none" stroke="#222" stroke-width="1.6"><path d="M40 16A18 18 0 0 0 9 12"/><path d="M8 32a18 18 0 0 0 31 4"/><path d="M9 5v7h7M39 43v-7h-7"/><path d="M29 17c-1-2-3-3-5-3-3 0-5 2-5 4 0 5 10 3 10 8 0 2-2 4-5 4-2 0-4-1-5-3M24 10v28"/></svg>
    <h3>Money Back Guarantee</h3>
    <p>Lorem Ipsum is simply dummy text<br>of the printing and typesetting.</p>
  </div>
  <div class="feature" style="left:833px">
    <svg viewBox="0 0 44 44" width="44" fill="none" stroke="#222" stroke-width="1.6"><path d="M10 6l6 8-3 4c2 5 6 9 11 11l4-3 8 6-4 6C18 38 6 26 4 10z"/><path d="M26 4a14 14 0 0 1 14 14M26 10a8 8 0 0 1 8 8"/></svg>
    <h3>Call Us</h3>
    <p>Lorem Ipsum is simply dummy text<br>of the printing and typesetting.</p>
  </div>
</section>

<section class="promo" style="top:952px">
  <div class="photo" role="img" aria-label="Woman in white sports top pulling off a blue jacket" style="left:0;background:linear-gradient(135deg,#6b6256 0%,#c9c2b8 40%,#3f62a8 75%,#2a4684 100%)"></div>
  <h2 class="thin" style="left:484px;top:84px">Woman's Apparel</h2>
  <h3 style="left:485px;top:145px">UP TO 70% OFF</h3>
  <p style="left:485px;top:197px">Lorem Ipsum is simply dummy text of the printing and typesetting industry. Lorem Ipsum has been the industry's standard dummy text ever since the 1500s.</p>
  <div class="btn-dark" style="left:484px;top:295px">Shop Now</div>
</section>

<section class="promo" style="top:1452px">
  <h2 class="thin" style="left:46px;top:85px">Best Selling</h2>
  <h3 style="left:47px;top:146px">UP TO 55% OFF</h3>
  <p style="left:47px;top:198px">Lorem Ipsum is simply dummy text of the printing and typesetting industry. Lorem Ipsum has been the industry's standard dummy text ever since the 1500s.</p>
  <div class="btn-dark" style="left:45px;top:294px">Shop Now</div>
  <div class="photo" role="img" aria-label="Athlete in blue training shirt lying on a green track field" style="left:439px;background:linear-gradient(135deg,#3d5a45 0%,#2c4636 30%,#1f6fd0 55%,#23334d 80%,#3f5e48 100%)"></div>
</section>

<section class="featured">
  <div class="abs latest">LATEST</div>
  <h2 class="abs thin featured-title">Featured Products</h2>
  <div class="arrow" style="left:94px"><svg width="14" height="10" viewBox="0 0 14 10" fill="none" stroke="#444" stroke-width="1.2"><path d="M13 5H1M5 1 1 5l4 4"/></svg></div>
  <div class="arrow" style="left:1062px"><svg width="14" height="10" viewBox="0 0 14 10" fill="none" stroke="#444" stroke-width="1.2"><path d="M1 5h12M9 1l4 4-4 4"/></svg></div>

  <div class="product" style="left:156px">
    <div class="thumb" role="img" aria-label="Blue and red sports jersey" style="background:linear-gradient(90deg,#2d57a8 50%,#d62b2b 50%);border-radius:30px 30px 10px 10px"></div>
    <div class="name">Lorem Ipsum is simply dummy text</div>
    <div class="price">$200 <s>$450</s></div>
    <div class="off">55% OFF</div>
    <div class="cart">ADD TO CART</div>
  </div>
  <div class="product" style="left:383px">
    <div class="thumb" role="img" aria-label="Pink women's training tee" style="width:110px;background:#e0307a;border-radius:24px 24px 8px 8px"></div>
    <div class="name">Lorem Ipsum is simply dummy text and printing</div>
    <div class="price">$150 <s>$320</s></div>
    <div class="off">51% OFF</div>
    <div class="cart">ADD TO CART</div>
  </div>
  <div class="product" style="left:611px">
    <div class="thumb" role="img" aria-label="Black running tights" style="width:60px;background:linear-gradient(180deg,#5ac43a 0 6%,#1c1c1c 6%);border-radius:6px"></div>
    <div class="name">Lorem Ipsum is simply dummy</div>
    <div class="price">$200 <s>$430</s></div>
    <div class="off">57% OFF</div>
    <div class="cart">ADD TO CART</div>
  </div>
  <div class="product" style="left:838px">
    <div class="thumb" role="img" aria-label="White running jacket" style="width:110px;background:linear-gradient(90deg,#dcdcdc,#f4f4f4 50%,#cfcfcf);border-radius:20px 20px 6px 6px"></div>
    <div class="name">Lorem Ipsum is simply dummy text</div>
    <div class="price">$200 <s>$160</s></div>
    <div class="off">20% OFF</div>
    <div class="cart">ADD TO CART</div>
  </div>
</section>

<section class="categories">
  <div class="category" style="left:161px">
    <div class="photo" role="img" aria-label="Woman in grey hoodie and sports top" style="background:linear-gradient(135deg,#55616b,#a09a93 55%,#3e4850)"></div>
    <div class="thin label">Woman</div>
  </div>
  <div class="category" style="left:465px">
    <div class="photo" role="img" aria-label="Man in green striped sports shirt" style="background:linear-gradient(135deg,#c9c4c0,#8a807a 40%,#1f8a6b 75%,#c3bdb8)"></div>
    <div class="thin label">Man</div>
  </div>
  <div class="category" style="left:769px">
    <div class="photo" role="img" aria-label="Supplement bottle among green leaves" style="background:linear-gradient(135deg,#8a9a6c,#f3f1ec 45%,#e0742a 65%,#5a7a3a)"></div>
    <div class="thin label">Supplyment</div>
  </div>
</section>

<section class="instagram">
  <h2 class="abs thin insta-title">Love us on Instagram at @Bramblecrest</h2>
  <div class="insta" style="left:0;background:linear-gradient(135deg,#c59a7e,#4a3a34)" role="img" aria-label="Athlete's back in black sports top"></div>
  <div class="insta" style="left:203px;background:linear-gradient(135deg,#3b4fc4,#e2a0c8 55%,#2a3aa0)" role="img" aria-label="Hand holding a pink drink bottle"></div>
  <div class="insta" style="left:405px;background:linear-gradient(135deg,#d8d8d8,#3a3a3a 55%,#e0e0e0)" role="img" aria-label="Man tying running shoes on the street"></div>
  <div class="insta" style="left:608px;background:linear-gradient(135deg,#222a3c,#0e1220 60%,#3450a0)" role="img" aria-label="Woman stretching on a dark floor"></div>
  <div class="insta" style="left:811px;background:linear-gradient(135deg,#5d7a3e,#e2a0c8 55%,#2e4a2a)" role="img" aria-label="Hand holding a pink drink bottle outdoors"></div>
  <div class="insta" style="left:1012px;background:linear-gradient(135deg,#ead6cc,#c46a5a 55%,#efe3dc)" role="img" aria-label="Runner's legs in sneakers mid stride"></div>
</section>

<footer>
  <div class="abs footer">
    <h2 class="thin news-title">Newsletter</h2>
    <p class="news-sub">Subscribe to stay with us and update our latest offers, products etc...</p>
    <div class="news-input">Enter Email</div>
    <div class="btn-dark news-btn">Subscribe</div>
    <div class="rule"></div>

    <div class="fcol" style="left:162px"><h4>Customer Service</h4><a>Faq</a><a>Return policy</a><a>Shipping Terms</a><a>Privacy Policy</a><a>Contact Us</a></div>
    <div class="fcol" style="left:389px"><h4>My Account</h4><a>Login</a><a>Sign Up</a></div>
    <div class="fcol" style="left:617px"><h4>Company</h4><a>About</a><a>Affiliate</a></div>
    <div class="fcol" style="left:844px"><h4>Payment Method</h4></div>
    <div class="pay" style="left:843px;top:242px;background:#2e77bb"></div>
    <div class="pay" style="left:893px;top:242px;background:#fff;border:1px solid #ccc"></div>
    <div class="pay" style="left:945px;top:242px;background:#fff;border:1px solid #ccc"></div>
    <div class="pay" style="left:843px;top:280px;background:#fff;border:1px solid #ccc"></div>
    <div class="pay" style="left:893px;top:280px;background:#e8832a"></div>
    <div class="pay" style="left:945px;top:280px;background:#fff;border:1px solid #ccc"></div>
  </div>
  <div class="abs bottom">
    <div class="copy">© BRAMBLECREST - 2019. All Rights Reserved.</div>
    <div class="social first" style="left:868px"></div>
    <div class="social" style="left:914px"></div>
    <div class="social" style="left:960px"></div>
    <div class="social" style="left:1006px"></div>
  </div>
</footer>

</body>
</html>
```